profestional carpet and furniture cleaning service

I have a Barlow cargo 2018 that I would like to wrap the sides the back and the back I'll send you pictures of my van, and some other pictures that could be utilized on the wrap ,it's a carpet and furniture cleaning company.
And probably I will Need some business cards design as well
The name of the company is solace, I am getting a new phone number for this company so for now I cannot provide you the number but I will get it shortly
I live in Montreal Canada and all the texts has to be in French.
the text that should show on the wrap is.
Nettoyage à la vapeur
Tapis
Meuble
Matelas
Céramique
Conduis de ventilation
and the phone number ...

Target Market(s)

residential

Industry/Entity Type

cleaning

Font styles to use
Sans Serif

Colors
0054AA
0677BA
7BADD7
CADEEF
E8F1F8
59FF00
82FF00
B8FF75
E3FFCB
F4FFEA
F0912C
F2A743
F7CA91
FBE8D2
FDF5EE
EB3D1F
EC4F4E
F09395
F8D3D4
FCEDEE

Requirements
Nice to have
• some pictures and add some steam vapor picture in the back round

```html
<!DOCTYPE html>
<html lang="fr">
<head>
<meta charset="utf-8">
<title>Solace — habillage de fourgon</title>
<link href="https://fonts.googleapis.com/css2?family=Montserrat:ital,wght@0,600;0,700;0,800;1,700&display=swap" rel="stylesheet">
<style>
  :root{
    --wrap-white:#eef0f3;
    --brand-blue:#1e3fd0;
    --brand-deep:#1a2fa8;
    --rocker-grey:#3a3c40;
    --ink:#111418;
    --page:#ffffff;
    --photo-a:#6f6a62;
    --photo-b:#c9bfae;
  }
  html,body{margin:0;padding:0;overflow:hidden;background:var(--page);}
  .canvas{width:1200px;height:614px;position:relative;overflow:hidden;}
  .wrap-side{display:block;width:1200px;height:614px;}
  .wrap-side text{font-family:"Montserrat",sans-serif;}
  .phone-number{font-style:italic;font-weight:700;font-size:28px;fill:var(--brand-blue);}
  .brand-name{font-weight:800;font-size:50px;fill:var(--brand-deep);letter-spacing:1px;}
  .brand-tagline{font-weight:700;font-size:19px;fill:var(--ink);letter-spacing:1px;}
  .service-label{font-weight:700;font-size:21px;fill:#ffffff;letter-spacing:.5px;}
  .web-address{font-weight:700;font-size:28px;fill:#ffffff;letter-spacing:2px;}
</style>
</head>
<body>
<div class="canvas">
<svg class="wrap-side" viewBox="0 0 1200 614" xmlns="http://www.w3.org/2000/svg">
  <defs>
    <radialGradient id="photoTone" cx="50%" cy="45%" r="60%">
      <stop offset="0" stop-color="var(--photo-b)"/>
      <stop offset="1" stop-color="var(--photo-a)"/>
    </radialGradient>
  </defs>

  <!-- body panels -->
  <rect class="panel-white" x="0" y="0" width="1200" height="470" fill="var(--wrap-white)"/>
  <path class="panel-blue" d="M610 0 H1200 V470 H630 Q700 235 650 40 Q640 15 610 0 Z" fill="var(--brand-blue)"/>
  <rect class="rocker-band" x="0" y="470" width="1200" height="144" fill="var(--rocker-grey)"/>
  <rect class="accent-stripe" x="0" y="528" width="1200" height="44" fill="var(--brand-blue)"/>
  <text class="web-address" x="600" y="560" text-anchor="middle">WWW.YOURCOMPANY.COM</text>

  <!-- contact block -->
  <g class="contact">
    <circle cx="80" cy="303" r="32" fill="var(--brand-blue)"/>
    <g class="phone-icon" fill="#ffffff">
      <path d="M58 296 q22 -14 44 0 l-4 7 q-18 -9 -36 0 Z"/>
      <rect x="66" y="301" width="28" height="18" rx="4"/>
      <circle cx="80" cy="310" r="5" fill="var(--brand-blue)"/>
    </g>
    <text class="phone-number" x="124" y="313">(123) 12345678</text>
    <g class="social-dots" fill="var(--brand-blue)">
      <circle cx="150" cy="380" r="22"/>
      <circle cx="215" cy="380" r="22"/>
      <circle cx="280" cy="380" r="22"/>
    </g>
  </g>

  <!-- brand -->
  <g class="brand">
    <circle cx="485" cy="200" r="72" fill="var(--brand-blue)"/>
    <text class="brand-name" x="485" y="355" text-anchor="middle">SOLACE</text>
    <text class="brand-tagline" x="485" y="395" text-anchor="middle">NETTOYAGE À LA</text>
  </g>

  <!-- service list -->
  <g class="service-list">
    <path d="M612 30 Q700 230 614 450" fill="none" stroke="var(--ink)" stroke-width="2"/>
    <circle cx="612" cy="30" r="5" fill="var(--ink)"/>
    <circle cx="614" cy="450" r="5" fill="var(--ink)"/>
    <g fill="var(--wrap-white)" stroke="var(--ink)" stroke-width="2">
      <circle cx="640" cy="95" r="24"/>
      <circle cx="662" cy="175" r="24"/>
      <circle cx="670" cy="255" r="24"/>
      <circle cx="662" cy="335" r="24"/>
      <circle cx="640" cy="415" r="24"/>
    </g>
    <text class="service-label" x="690" y="103">TAPIS</text>
    <text class="service-label" x="710" y="183">MEUBLE</text>
    <text class="service-label" x="712" y="263">MATELAS</text>
    <text class="service-label" x="705" y="343">CÉRAMIQUE</text>
    <text class="service-label" x="680" y="423">CONDUIS DE VENTILATION</text>
  </g>

  <!-- photo circles -->
  <g class="service-photos">
    <circle role="img" aria-label="Photo d'un nettoyeur de tapis à la vapeur en action" cx="1110" cy="170" r="85" fill="url(#photoTone)"/>
    <circle role="img" aria-label="Photo du nettoyage d'un meuble rembourré" cx="1040" cy="350" r="65" fill="url(#photoTone)"/>
    <circle role="img" aria-label="Photo de l'équipement d'extraction installé dans le fourgon" cx="1132" cy="392" r="62" fill="url(#photoTone)"/>
  </g>
</svg>
</div>
</body>
</html>
```